Increased budget: GUI redesign: 10 year old user interface needs modern look-and-feel

UPDATE: Please DO look at more than only th eone image I attached! Almost all designs are simply reworks of that one picture. That is not what we are looking for. Check out the video to understand what the product does, and try to make something better.
We have an existing app (see https://www.vornatek.com/downloadTunePilot.php?vers=3_9_1_140964&dir=Vornatek_OEM/3_9_1_140964&name=DSP_Control_Software) which needs refreshing. See also a video here: https://vornatek-oem.com/software/ and the user manual attached here. The GUI is now 800x400 pixels, which is too small; and not scalable, which will be fixed in the future. We need a new, modern look-and-feel, and images that can be exported from the design in various sizes. The current design is attached as well as a collection of PNG files. The overall layout can stay similar, although we are open to good ideas for improvements. The design should be targeted at professional users, not end users; the product is used by audio professionals (e.g. sound engineers, loudspeaker designers). Also see our web version: https://www.vornatek.com/tunepilot/skins/1_1_2/container.html?MAC=Demo%201x2
The winner will also be asked to do a full design of the application GUI (based on the design done here), with several more windows etc, and additional payment depending on the work to be done.

Target Market(s)

Professional audio

Industry/Entity Type

Audio / Industrial

Font styles to use
Other font styles liked:
• Futura (not mandatory)

Colors

Designer to choose colors to be used in the design.

Requirements
Must have
• Modern, timeless design, not too bling bling
Nice to have
• Flat design
Should not have
• 3D, bling bling, many colours, etc

```html
<!DOCTYPE html>
<html lang="en">
<head>
<meta charset="utf-8">
<title>Vornatek DSP Control – Main</title>
<link rel="stylesheet" href="https://fonts.googleapis.com/css2?family=Barlow:wght@400;500;600;700&display=swap">
<style>
:root{
  --canvas:#dfe3e7;
  --navy:#0f2a3a;
  --ink:#13232e;
  --muted:#5f6b74;
  --line:#d6dadd;
  --panel:#eceeef;
  --white:#ffffff;
  --knob:#173447;
  --track:#3d5566;
  --orange:#f39a1e;
  --red:#e0473e;
  --green:#35b34a;
  --olive:#a9bd3c;
  --ring:#c7dbe8;
  --grey-chip:#c9ced2;
}
*{box-sizing:border-box;margin:0;padding:0}
html,body{width:1200px;height:775px;overflow:hidden}
body{background:var(--canvas);font-family:"Barlow",sans-serif;color:var(--ink);position:relative}
.window{position:absolute;left:33px;top:9px;width:900px;height:600px;transform:scale(1.26);transform-origin:0 0;border-radius:10px;overflow:hidden;background:var(--white);box-shadow:0 6px 24px rgba(15,42,58,.18)}
.sidebar{position:absolute;left:0;top:0;width:133px;height:600px;background:var(--navy)}
.traffic{position:absolute;top:20px;width:12px;height:12px;border-radius:50%}
.traffic.close{left:16px;background:#ff5f57}
.traffic.min{left:37px;background:#febc2e}
.traffic.max{left:58px;background:#28c840}
.nav{position:absolute;left:16px;top:73px;width:100px;list-style:none}
.nav li{height:35px;display:flex;align-items:center;gap:9px;padding-left:12px;color:var(--white);font-size:9.5px;font-weight:600;letter-spacing:.3px}
.nav li.active{background:#0a1f2c;border-radius:5px;height:33px;margin-bottom:2px}
.nav .icon-box{width:15px;height:15px;border-radius:3px;display:flex;align-items:center;justify-content:center}
.nav .icon-box.main{background:var(--orange)}
.nav .icon-box.xover{background:var(--red)}
.nav .ring{width:14px;height:14px;border-radius:50%;border:3.5px solid var(--ring);margin-right:-3px}
.nav .ring.out{border-color:var(--olive)}

.unit-title{position:absolute;left:160px;top:20px;font-size:12.5px;font-weight:700;letter-spacing:.2px;white-space:nowrap}
.select{position:absolute;height:26px;border:1px solid var(--line);border-radius:4px;background:var(--white);font-size:7.5px;font-weight:600;display:flex;align-items:center;padding:0 10px;justify-content:space-between;white-space:nowrap}
.select svg{width:8px;height:8px}
.gear{position:absolute;left:853px;top:14px;width:26px;height:26px;border-radius:50%;background:#eef0f2;display:flex;align-items:center;justify-content:center}

.brand{position:absolute;left:160px;top:80px;width:163px;display:flex;align-items:center;justify-content:center;gap:6px;font-size:13px;font-weight:700;color:var(--navy);letter-spacing:.5px}
.brand .mark{width:10px;height:10px;background:var(--navy)}
.label{position:absolute;left:160px;font-size:7.5px;color:var(--muted);letter-spacing:.3px}
.btn{position:absolute;height:23px;border-radius:3px;font-size:7px;font-weight:700;display:flex;align-items:center;justify-content:center;letter-spacing:.3px}
.btn.outline{border:1px solid var(--navy);color:var(--navy);background:var(--white)}
.btn.solid{background:var(--knob);color:var(--white)}
.badge{position:absolute;left:296px;width:27px;height:16px;border-radius:4px;display:flex;align-items:center;justify-content:center}
.badge.on{background:var(--green)}
.badge.alert{background:var(--red)}

.mixer{position:absolute;left:350px;top:67px;width:530px;height:513px;background:var(--panel);border-radius:8px}
.scale{position:absolute;left:0;font-size:6px;color:#8a949b;width:37px;text-align:right}
.strip{position:absolute;top:20px;width:40px;height:346px;background:var(--white);border:1px solid #e0e3e6;border-radius:4px}
.strip.alert{border-color:var(--red)}
.strip::before,.strip::after{content:"";position:absolute;top:23px;height:300px;width:6px;background:repeating-linear-gradient(to bottom,#c6ccd0 0 1px,transparent 1px 5px)}
.strip::before{left:7px}
.strip::after{right:7px}
.track{position:absolute;left:18px;top:23px;width:3px;height:300px;background:var(--track);border-radius:2px}
.knob{position:absolute;left:11px;width:16px;height:40px;background:var(--knob);border-radius:3px}
.knob::after{content:"";position:absolute;left:5px;top:17px;width:6px;height:5px;border-top:1px solid #9fb0bb;border-bottom:1px solid #9fb0bb}
.row-label{position:absolute;left:14px;font-size:7.5px;color:var(--ink)}
.pair{position:absolute;top:381px;width:90px;height:22px;background:var(--white);border:1px solid var(--line);border-radius:3px;font-size:7px;font-weight:600;display:flex;align-items:center;justify-content:space-between;padding:0 11px}
.chain{width:17px;height:10px;border-radius:3px;display:flex;align-items:center;justify-content:center}
.chain.on{background:var(--green)}
.chain.off{background:var(--grey-chip)}
.divider{position:absolute;left:50px;width:440px;height:1px;background:var(--line)}
.sound{position:absolute;top:431px;width:40px;height:16px;border:1px solid var(--knob);border-radius:2px;background:var(--white);display:flex;align-items:center;justify-content:center}
.sound.muted{border-color:var(--red)}
.sound svg{width:9px;height:9px}
.channel{position:absolute;top:474px;width:40px;height:22px;background:var(--white);border:1px solid var(--line);border-radius:3px;font-size:7px;font-weight:600;display:flex;align-items:center;justify-content:center}
</style>
</head>
<body>
<main class="window">
  <aside class="sidebar">
    <span class="traffic close"></span><span class="traffic min"></span><span class="traffic max"></span>
    <ul class="nav">
      <li class="active"><span class="icon-box main"><svg width="9" height="9" viewBox="0 0 9 9" fill="none" stroke="#fff" stroke-width="1"><path d="M3 1v7M6 1v7M1 3h7M1 6h7"/></svg></span>MAIN</li>
      <li><span class="icon-box xover"><svg width="10" height="8" viewBox="0 0 10 8" fill="none" stroke="#fff" stroke-width="1.1"><path d="M1 1h2l4 6h2M1 7h2l4-6h2"/></svg></span>X-OVER</li>
      <li><span class="ring"></span>IN 1</li>
      <li><span class="ring"></span>IN 2</li>
      <li><span class="ring"></span>IN 3</li>
      <li><span class="ring"></span>IN 4</li>
      <li><span class="ring out"></span>OUT 1</li>
      <li><span class="ring out"></span>OUT 2</li>
      <li><span class="ring out"></span>OUT 3</li>
      <li><span class="ring out"></span>OUT 4</li>
    </ul>
  </aside>

  <h1 class="unit-title">VORNATEK KX8-Q6 (3C:4A:92:E7:05:B1)</h1>
  <div class="select" style="left:677px;top:14px;width:163px">AES<svg viewBox="0 0 8 8" fill="none" stroke="#13232e" stroke-width="1.3"><path d="M1.5 3l2.5 2.5L6.5 3"/></svg></div>
  <div class="gear"><svg width="12" height="12" viewBox="0 0 12 12"><circle cx="6" cy="6" r="4" fill="none" stroke="#13232e" stroke-width="2.4" stroke-dasharray="2 1.4"/><circle cx="6" cy="6" r="2.6" fill="#13232e"/><circle cx="6" cy="6" r="1.1" fill="#eef0f2"/></svg></div>

  <div class="brand"><span class="mark"></span>VORNATEK</div>

  <span class="label" style="top:141px">LOCAL PRESETS</span>
  <div class="btn outline" style="left:160px;top:158px;width:76px">STORE</div>
  <div class="btn solid" style="left:246px;top:158px;width:77px">LOAD</div>

  <span class="label" style="top:203px">UNIT PRESETS</span>
  <div class="select" style="left:160px;top:220px;width:163px">Setup demo</div>
  <div class="select" style="left:160px;top:250px;width:163px">Example label 01<svg viewBox="0 0 8 8" fill="none" stroke="#13232e" stroke-width="1.3"><path d="M1.5 3l2.5 2.5L6.5 3"/></svg></div>
  <div class="btn outline" style="left:160px;top:286px;width:76px">STORE</div>
  <div class="btn solid" style="left:246px;top:286px;width:77px">LOAD</div>

  <span class="label" style="top:331px">LINK</span>
  <div class="badge on" style="top:327px"><svg width="12" height="7" viewBox="0 0 12 7" fill="none" stroke="#13232e" stroke-width="1.1"><rect x="1" y="1" width="5" height="5" rx="2.5"/><rect x="6" y="1" width="5" height="5" rx="2.5"/></svg></div>
  <div class="select" style="left:160px;top:349px;width:163px">RX-60<svg viewBox="0 0 8 8" fill="none" stroke="#13232e" stroke-width="1.3"><path d="M1.5 3l2.5 2.5L6.5 3"/></svg></div>

  <span class="label" style="top:398px">UNIT NAME</span>
  <div class="select" style="left:160px;top:417px;width:163px">Vornatek RX-60<svg viewBox="0 0 8 8" fill="none" stroke="#13232e" stroke-width="1.3"><path d="M1.5 3l2.5 2.5L6.5 3"/></svg></div>

  <span class="label" style="top:464px">STATUS</span>
  <div class="badge alert" style="top:460px"><svg width="10" height="10" viewBox="0 0 10 10" fill="#fff" stroke="#fff" stroke-width="1"><path d="M1 3.5h2l3-2.5v8L3 6.5H1z" stroke="none"/><path d="M1 1l8 8"/></svg></div>
  <div class="btn outline" style="left:160px;top:482px;width:163px">DETAILS</div>

  <section class="mixer">
    <span class="scale" style="top:30px">+12</span>
    <span class="scale" style="top:60px">+6</span>
    <span class="scale" style="top:90px">0</span>
    <span class="scale" style="top:120px">-6</span>
    <span class="scale" style="top:150px">-12</span>
    <span class="scale" style="top:180px">-18</span>
    <span class="scale" style="top:210px">-24</span>
    <span class="scale" style="top:240px">-30</span>
    <span class="scale" style="top:270px">-36</span>
    <span class="scale" style="top:300px">-42</span>
    <span class="scale" style="top:330px">-48</span>

    <div class="strip" style="left:50px"><span class="track"></span><span class="knob" style="top:64px"></span></div>
    <div class="strip alert" style="left:100px"><span class="track"></span><span class="knob" style="top:214px"></span></div>
    <div class="strip" style="left:150px"><span class="track"></span><span class="knob" style="top:134px"></span></div>
    <div class="strip" style="left:200px"><span class="track"></span><span class="knob" style="top:22px"></span></div>
    <div class="strip alert" style="left:300px"><span class="track"></span><span class="knob" style="top:64px"></span></div>
    <div class="strip" style="left:350px"><span class="track"></span><span class="knob" style="top:134px"></span></div>
    <div class="strip" style="left:400px"><span class="track"></span><span class="knob" style="top:284px"></span></div>
    <div class="strip alert" style="left:450px"><span class="track"></span><span class="knob" style="top:184px"></span></div>

    <span class="row-label" style="top:388px">Link</span>
    <div class="pair" style="left:50px"><span>0.00</span><span class="chain on"><svg width="11" height="6" viewBox="0 0 12 7" fill="none" stroke="#13232e" stroke-width="1.2"><rect x="1" y="1" width="5" height="5" rx="2.5"/><rect x="6" y="1" width="5" height="5" rx="2.5"/></svg></span><span>-30.00</span></div>
    <div class="pair" style="left:150px"><span>-15</span><span class="chain off"><svg width="11" height="6" viewBox="0 0 12 7" fill="none" stroke="#fff" stroke-width="1.2"><rect x="1" y="1" width="5" height="5" rx="2.5"/><rect x="6" y="1" width="5" height="5" rx="2.5"/></svg></span><span>9.00</span></div>
    <div class="pair" style="left:300px"><span>0.00</span><span class="chain off"><svg width="11" height="6" viewBox="0 0 12 7" fill="none" stroke="#fff" stroke-width="1.2"><rect x="1" y="1" width="5" height="5" rx="2.5"/><rect x="6" y="1" width="5" height="5" rx="2.5"/></svg></span><span>-15</span></div>
    <div class="pair" style="left:400px"><span>-45</span><span class="chain off"><svg width="11" height="6" viewBox="0 0 12 7" fill="none" stroke="#fff" stroke-width="1.2"><rect x="1" y="1" width="5" height="5" rx="2.5"/><rect x="6" y="1" width="5" height="5" rx="2.5"/></svg></span><span>-24</span></div>

    <span class="divider" style="top:416px"></span>
    <span class="row-label" style="top:434px">Sound</span>
    <div class="sound" style="left:50px"><svg viewBox="0 0 10 10" fill="#13232e" stroke="#13232e" stroke-width="1"><path d="M1 3.5h2l3-2.5v8L3 6.5H1z" stroke="none"/><path d="M7.5 3.2q1.2 1.8 0 3.6" fill="none"/></svg></div>
    <div class="sound muted" style="left:100px"><svg viewBox="0 0 10 10" fill="#e0473e" stroke="#e0473e" stroke-width="1"><path d="M1 3.5h2l3-2.5v8L3 6.5H1z" stroke="none"/><path d="M1 1l8 8"/></svg></div>
    <div class="sound" style="left:150px"><svg viewBox="0 0 10 10" fill="#13232e" stroke="#13232e" stroke-width="1"><path d="M1 3.5h2l3-2.5v8L3 6.5H1z" stroke="none"/><path d="M7.5 3.2q1.2 1.8 0 3.6" fill="none"/></svg></div>
    <div class="sound" style="left:200px"><svg viewBox="0 0 10 10" fill="#13232e" stroke="#13232e" stroke-width="1"><path d="M1 3.5h2l3-2.5v8L3 6.5H1z" stroke="none"/><path d="M7.5 3.2q1.2 1.8 0 3.6" fill="none"/></svg></div>
    <div class="sound muted" style="left:300px"><svg viewBox="0 0 10 10" fill="#e0473e" stroke="#e0473e" stroke-width="1"><path d="M1 3.5h2l3-2.5v8L3 6.5H1z" stroke="none"/><path d="M1 1l8 8"/></svg></div>
    <div class="sound" style="left:350px"><svg viewBox="0 0 10 10" fill="#13232e" stroke="#13232e" stroke-width="1"><path d="M1 3.5h2l3-2.5v8L3 6.5H1z" stroke="none"/><path d="M7.5 3.2q1.2 1.8 0 3.6" fill="none"/></svg></div>
    <div class="sound" style="left:400px"><svg viewBox="0 0 10 10" fill="#13232e" stroke="#13232e" stroke-width="1"><path d="M1 3.5h2l3-2.5v8L3 6.5H1z" stroke="none"/><path d="M7.5 3.2q1.2 1.8 0 3.6" fill="none"/></svg></div>
    <div class="sound muted" style="left:450px"><svg viewBox="0 0 10 10" fill="#e0473e" stroke="#e0473e" stroke-width="1"><path d="M1 3.5h2l3-2.5v8L3 6.5H1z" stroke="none"/><path d="M1 1l8 8"/></svg></div>
    <span class="divider" style="top:461px"></span>

    <div class="channel" style="left:50px">In 1</div>
    <div class="channel" style="left:100px">In 2</div>
    <div class="channel" style="left:150px">In 3</div>
    <div class="channel" style="left:200px">In 4</div>
    <div class="channel" style="left:300px">Out 1</div>
    <div class="channel" style="left:350px">Out 2</div>
    <div class="channel" style="left:400px">Out 3</div>
    <div class="channel" style="left:450px">Out 4</div>
  </section>
</main>
</body>
</html>
```